Wandkalender für Bio-Wollstoffe in A!
sehr gute und selbständige Arbeit trotz zeitbedingt wenig Input von uns. Herzlichen Dank!
Zielgruppe
Wir verkaufen Bio Wollstoffe zum Nähen. Unsere Zielgruppe sind also ökologisch bewußte kreative Näherinnen.
Aufgabenstellung
Wir möchten einen Wandkalender in DinA1 fertigen. Fotos werden von uns geliefert und können bunt zwischen die Monate verteilt werden.
Technisch haben wir von der Druckerei folgende Vorgaben:
Endformat: DIN A4 21,0 x 29,7 cm
Format offen: DIN A1 59,4 x 84,1 cm
Umfang: einseitig bedruckt
Satz/Repro: druckfähige PDF-Daten geliefert, wir
senden Ihnen einen Bildschirmsoftproof
Druck/Farben: 4/0 farbig Skala
Papier: 135 g/qm Bilderdruck Matt

```html
<!DOCTYPE html>
<html lang="de">
<head>
<meta charset="utf-8">
<title>Wandkalender 2020</title>
<link rel="stylesheet" href="https://fonts.googleapis.com/css2?family=Oswald:wght@400;500&family=Montserrat:wght@500;600&display=swap">
<style>
  :root {
    --paper: #f3f4f5;
    --sheet: #ffffff;
    --tab: #a4bfcc;
    --tab-light: #b9cfd9;
    --bar: #2e3940;
    --sunday: #8db0c1;
    --ink: #1e2326;
    --frame: rgba(255,255,255,0.75);
  }
  * { box-sizing: border-box; margin: 0; padding: 0; }
  html, body { width: 869px; height: 1200px; overflow: hidden; background: var(--paper); }
  .calendar { position: relative; width: 869px; height: 1200px; background: var(--paper); font-family: "Montserrat", sans-serif; color: var(--ink); }

  .collage { position: absolute; inset: 0 0 auto 0; height: 586px; }
  .photo { position: absolute; }
  .frame-line { position: absolute; left: 39px; top: 31px; width: 791px; height: 524px; border: 2px solid var(--frame); pointer-events: none; }
  .year { position: absolute; left: 342px; top: 0; width: 186px; height: 53px; background: var(--tab-light); color: #fff; font-family: "Oswald", sans-serif; font-weight: 500; font-size: 40px; line-height: 53px; text-align: center; letter-spacing: 1px; }

  .months { position: absolute; left: 0; top: 586px; width: 869px; height: 602px; background: var(--sheet); }
  .band { position: absolute; left: 0; bottom: 0; width: 869px; height: 12px; background: var(--tab); }

  .month { position: absolute; width: 169px; }
  .month-tab { height: 46px; background: var(--tab); border-radius: 0 12px 0 0; display: flex; align-items: center; padding-left: 15px; color: #fff; font-family: "Oswald", sans-serif; }
  .month-num { font-size: 27px; font-weight: 400; }
  .month-name { font-size: 17px; text-transform: uppercase; border-left: 1.5px solid #fff; margin-left: 11px; padding-left: 11px; line-height: 22px; }
  .weekdays, .dates { display: grid; grid-template-columns: repeat(7, 1fr); text-align: center; }
  .weekdays { height: 16px; background: var(--bar); color: #fff; font-size: 8px; line-height: 16px; font-weight: 600; }
  .weekdays span:first-child { color: var(--sunday); background: var(--tab); }
  .dates { margin-top: 5px; font-size: 9px; font-weight: 500; line-height: 18px; }
  .dates .first { grid-column-start: var(--start); }
  .sun-1 .dates span:nth-child(7n+1),
  .sun-2 .dates span:nth-child(7n+2),
  .sun-3 .dates span:nth-child(7n+3),
  .sun-4 .dates span:nth-child(7n+4),
  .sun-5 .dates span:nth-child(7n+5),
  .sun-6 .dates span:nth-child(7n+6),
  .sun-7 .dates span:nth-child(7n+7) { color: var(--sunday); }

  .col-1 { left: 56px; } .col-2 { left: 252px; } .col-3 { left: 449px; } .col-4 { left: 645px; }
  .row-1 { top: 44px; } .row-2 { top: 230px; } .row-3 { top: 421px; }
</style>
</head>
<body>
<main class="calendar">
  <section class="collage">
    <div class="photo" role="img" aria-label="Cat lying on a wooden floor on a striped wool garment" style="left:0;top:0;width:186px;height:326px;background:linear-gradient(160deg,#ddd6cc,#b9a896 60%,#d8d0c4)"></div>
    <div class="photo" role="img" aria-label="Colourful wool skirts hanging on a clothesline in a garden" style="left:194px;top:0;width:358px;height:195px;background:linear-gradient(180deg,#9fae8c,#7e5f8e 45%,#b45a8a 60%,#5f7a4a)"></div>
    <div class="photo" role="img" aria-label="Child reaching up beside a sunflower pinwheel" style="left:559px;top:0;width:154px;height:97px;background:linear-gradient(135deg,#4c4d52,#6a84a3 55%,#d7b64a)"></div>
    <div class="photo" role="img" aria-label="Three children laughing on a garden bench" style="left:721px;top:0;width:148px;height:195px;background:linear-gradient(160deg,#8fa57a,#b47a5d 55%,#5c6e8c)"></div>
    <div class="photo" role="img" aria-label="Wool skirt next to a yellow bicycle frame" style="left:194px;top:202px;width:176px;height:124px;background:linear-gradient(135deg,#4a4a4c,#6b6f73 50%,#d9b53a)"></div>
    <div class="photo" role="img" aria-label="Girls in wool clothes balancing on a log" style="left:377px;top:202px;width:175px;height:243px;background:linear-gradient(170deg,#b6c7a4,#8a9fc0 40%,#9a5e3c 65%,#6f8d52)"></div>
    <div class="photo" role="img" aria-label="Child in a hooded rust dress on gravel" style="left:559px;top:104px;width:154px;height:222px;background:linear-gradient(170deg,#a0683e,#b5512e 50%,#c08a5a)"></div>
    <div class="photo" role="img" aria-label="Legs in blue wool trousers on a bench by the sea" style="left:721px;top:202px;width:148px;height:177px;background:linear-gradient(180deg,#b7c4cc,#6d8a4e 45%,#2f6da0 75%,#7a6e60)"></div>
    <div class="photo" role="img" aria-label="Red wool skirt and leg warmers on a wall" style="left:0;top:333px;width:186px;height:253px;background:linear-gradient(150deg,#a93a52,#2c2c30 50%,#7a8a6a)"></div>
    <div class="photo" role="img" aria-label="Woman jumping in a grey wool skirt on a cobbled street" style="left:194px;top:333px;width:176px;height:253px;background:linear-gradient(180deg,#c9cdd1,#6f7a84 50%,#8c8a86)"></div>
    <div class="photo" role="img" aria-label="Two girls in patterned wool dresses on grass" style="left:559px;top:333px;width:154px;height:112px;background:linear-gradient(135deg,#6d7a4a,#4a3326 50%,#c9a44a)"></div>
    <div class="photo" role="img" aria-label="Yellow and grey wool skirt laid flat" style="left:721px;top:386px;width:148px;height:95px;background:linear-gradient(135deg,#ecebe6,#7e8288 45%,#d2a03a 70%,#b05a2a)"></div>
    <div class="photo" role="img" aria-label="Two small children hugging beside a stone sculpture" style="left:377px;top:453px;width:336px;height:133px;background:linear-gradient(90deg,#8e8a80,#9c4a4a 40%,#5a4a40 70%,#8c8a84)"></div>
    <div class="photo" role="img" aria-label="Two toddlers in red wool clothes running on grass" style="left:721px;top:488px;width:148px;height:98px;background:linear-gradient(180deg,#5f8f3c,#7a2a2e 50%,#4f8234)"></div>
    <div class="frame-line"></div>
    <div class="year">2020</div>
  </section>

  <section class="months">
    <article class="month col-1 row-1 sun-5"><header class="month-tab"><span class="month-num">01</span><span class="month-name">January</span></header>
      <div class="weekdays"><span>Su</span><span>Mo</span><span>Tu</span><span>We</span><span>Th</span><span>Fr</span><span>Sa</span></div>
      <div class="dates" style="--start:4"><span class="first">1</span><span>2</span><span>3</span><span>4</span><span>5</span><span>6</span><span>7</span><span>8</span><span>9</span><span>10</span><span>11</span><span>12</span><span>13</span><span>14</span><span>15</span><span>16</span><span>17</span><span>18</span><span>19</span><span>20</span><span>21</span><span>22</span><span>23</span><span>24</span><span>25</span><span>26</span><span>27</span><span>28</span><span>29</span><span>30</span><span>31</span></div></article>

    <article class="month col-2 row-1 sun-2"><header class="month-tab"><span class="month-num">02</span><span class="month-name">February</span></header>
      <div class="weekdays"><span>Su</span><span>Mo</span><span>Tu</span><span>We</span><span>Th</span><span>Fr</span><span>Sa</span></div>
      <div class="dates" style="--start:7"><span class="first">1</span><span>2</span><span>3</span><span>4</span><span>5</span><span>6</span><span>7</span><span>8</span><span>9</span><span>10</span><span>11</span><span>12</span><span>13</span><span>14</span><span>15</span><span>16</span><span>17</span><span>18</span><span>19</span><span>20</span><span>21</span><span>22</span><span>23</span><span>24</span><span>25</span><span>26</span><span>27</span><span>28</span><span>29</span></div></article>

    <article class="month col-3 row-1 sun-1"><header class="month-tab"><span class="month-num">03</span><span class="month-name">March</span></header>
      <div class="weekdays"><span>Su</span><span>Mo</span><span>Tu</span><span>We</span><span>Th</span><span>Fr</span><span>Sa</span></div>
      <div class="dates" style="--start:1"><span class="first">1</span><span>2</span><span>3</span><span>4</span><span>5</span><span>6</span><span>7</span><span>8</span><span>9</span><span>10</span><span>11</span><span>12</span><span>13</span><span>14</span><span>15</span><span>16</span><span>17</span><span>18</span><span>19</span><span>20</span><span>21</span><span>22</span><span>23</span><span>24</span><span>25</span><span>26</span><span>27</span><span>28</span><span>29</span><span>30</span><span>31</span></div></article>

    <article class="month col-4 row-1 sun-5"><header class="month-tab"><span class="month-num">04</span><span class="month-name">April</span></header>
      <div class="weekdays"><span>Su</span><span>Mo</span><span>Tu</span><span>We</span><span>Th</span><span>Fr</span><span>Sa</span></div>
      <div class="dates" style="--start:4"><span class="first">1</span><span>2</span><span>3</span><span>4</span><span>5</span><span>6</span><span>7</span><span>8</span><span>9</span><span>10</span><span>11</span><span>12</span><span>13</span><span>14</span><span>15</span><span>16</span><span>17</span><span>18</span><span>19</span><span>20</span><span>21</span><span>22</span><span>23</span><span>24</span><span>25</span><span>26</span><span>27</span><span>28</span><span>29</span><span>30</span></div></article>

    <article class="month col-1 row-2 sun-3"><header class="month-tab"><span class="month-num">05</span><span class="month-name">May</span></header>
      <div class="weekdays"><span>Su</span><span>Mo</span><span>Tu</span><span>We</span><span>Th</span><span>Fr</span><span>Sa</span></div>
      <div class="dates" style="--start:6"><span class="first">1</span><span>2</span><span>3</span><span>4</span><span>5</span><span>6</span><span>7</span><span>8</span><span>9</span><span>10</span><span>11</span><span>12</span><span>13</span><span>14</span><span>15</span><span>16</span><span>17</span><span>18</span><span>19</span><span>20</span><span>21</span><span>22</span><span>23</span><span>24</span><span>25</span><span>26</span><span>27</span><span>28</span><span>29</span><span>30</span><span>31</span></div></article>

    <article class="month col-2 row-2 sun-7"><header class="month-tab"><span class="month-num">06</span><span class="month-name">June</span></header>
      <div class="weekdays"><span>Su</span><span>Mo</span><span>Tu</span><span>We</span><span>Th</span><span>Fr</span><span>Sa</span></div>
      <div class="dates" style="--start:2"><span class="first">1</span><span>2</span><span>3</span><span>4</span><span>5</span><span>6</span><span>7</span><span>8</span><span>9</span><span>10</span><span>11</span><span>12</span><span>13</span><span>14</span><span>15</span><span>16</span><span>17</span><span>18</span><span>19</span><span>20</span><span>21</span><span>22</span><span>23</span><span>24</span><span>25</span><span>26</span><span>27</span><span>28</span><span>29</span><span>30</span></div></article>

    <article class="month col-3 row-2 sun-5"><header class="month-tab"><span class="month-num">07</span><span class="month-name">July</span></header>
      <div class="weekdays"><span>Su</span><span>Mo</span><span>Tu</span><span>We</span><span>Th</span><span>Fr</span><span>Sa</span></div>
      <div class="dates" style="--start:4"><span class="first">1</span><span>2</span><span>3</span><span>4</span><span>5</span><span>6</span><span>7</span><span>8</span><span>9</span><span>10</span><span>11</span><span>12</span><span>13</span><span>14</span><span>15</span><span>16</span><span>17</span><span>18</span><span>19</span><span>20</span><span>21</span><span>22</span><span>23</span><span>24</span><span>25</span><span>26</span><span>27</span><span>28</span><span>29</span><span>30</span><span>31</span></div></article>

    <article class="month col-4 row-2 sun-2"><header class="month-tab"><span class="month-num">08</span><span class="month-name">August</span></header>
      <div class="weekdays"><span>Su</span><span>Mo</span><span>Tu</span><span>We</span><span>Th</span><span>Fr</span><span>Sa</span></div>
      <div class="dates" style="--start:7"><span class="first">1</span><span>2</span><span>3</span><span>4</span><span>5</span><span>6</span><span>7</span><span>8</span><span>9</span><span>10</span><span>11</span><span>12</span><span>13</span><span>14</span><span>15</span><span>16</span><span>17</span><span>18</span><span>19</span><span>20</span><span>21</span><span>22</span><span>23</span><span>24</span><span>25</span><span>26</span><span>27</span><span>28</span><span>29</span><span>30</span><span>31</span></div></article>

    <article class="month col-1 row-3 sun-6"><header class="month-tab"><span class="month-num">09</span><span class="month-name">September</span></header>
      <div class="weekdays"><span>Su</span><span>Mo</span><span>Tu</span><span>We</span><span>Th</span><span>Fr</span><span>Sa</span></div>
      <div class="dates" style="--start:3"><span class="first">1</span><span>2</span><span>3</span><span>4</span><span>5</span><span>6</span><span>7</span><span>8</span><span>9</span><span>10</span><span>11</span><span>12</span><span>13</span><span>14</span><span>15</span><span>16</span><span>17</span><span>18</span><span>19</span><span>20</span><span>21</span><span>22</span><span>23</span><span>24</span><span>25</span><span>26</span><span>27</span><span>28</span><span>29</span><span>30</span></div></article>

    <article class="month col-2 row-3 sun-4"><header class="month-tab"><span class="month-num">10</span><span class="month-name">October</span></header>
      <div class="weekdays"><span>Su</span><span>Mo</span><span>Tu</span><span>We</span><span>Th</span><span>Fr</span><span>Sa</span></div>
      <div class="dates" style="--start:5"><span class="first">1</span><span>2</span><span>3</span><span>4</span><span>5</span><span>6</span><span>7</span><span>8</span><span>9</span><span>10</span><span>11</span><span>12</span><span>13</span><span>14</span><span>15</span><span>16</span><span>17</span><span>18</span><span>19</span><span>20</span><span>21</span><span>22</span><span>23</span><span>24</span><span>25</span><span>26</span><span>27</span><span>28</span><span>29</span><span>30</span><span>31</span></div></article>

    <article class="month col-3 row-3 sun-1"><header class="month-tab"><span class="month-num">11</span><span class="month-name">November</span></header>
      <div class="weekdays"><span>Su</span><span>Mo</span><span>Tu</span><span>We</span><span>Th</span><span>Fr</span><span>Sa</span></div>
      <div class="dates" style="--start:1"><span class="first">1</span><span>2</span><span>3</span><span>4</span><span>5</span><span>6</span><span>7</span><span>8</span><span>9</span><span>10</span><span>11</span><span>12</span><span>13</span><span>14</span><span>15</span><span>16</span><span>17</span><span>18</span><span>19</span><span>20</span><span>21</span><span>22</span><span>23</span><span>24</span><span>25</span><span>26</span><span>27</span><span>28</span><span>29</span><span>30</span></div></article>

    <article class="month col-4 row-3 sun-6"><header class="month-tab"><span class="month-num">12</span><span class="month-name">December</span></header>
      <div class="weekdays"><span>Su</span><span>Mo</span><span>Tu</span><span>We</span><span>Th</span><span>Fr</span><span>Sa</span></div>
      <div class="dates" style="--start:3"><span class="first">1</span><span>2</span><span>3</span><span>4</span><span>5</span><span>6</span><span>7</span><span>8</span><span>9</span><span>10</span><span>11</span><span>12</span><span>13</span><span>14</span><span>15</span><span>16</span><span>17</span><span>18</span><span>19</span><span>20</span><span>21</span><span>22</span><span>23</span><span>24</span><span>25</span><span>26</span><span>27</span><span>28</span><span>29</span><span>30</span><span>31</span></div></article>
  </section>
  <div class="band"></div>
</main>
</body>
</html>
```